Global Weight loss program

we need a business card based in Brooklyn , NY called PeppertonRUN . Mara Dulvik Tenbrook the founder and creator of PeppertonRUN Movement. A business based around nutrition, health, Whole Foods and fitness.

Industry/Entity Type

Food Service

Contact Information for Business Card

Phone number : 718-555-0143
website www.peppertonrun.com
email : mara@peppertonrun.com

Font styles to use
Sans Serif

Requirements
Must have
• logo colors
• green black and gold
Nice to have
• must be simple and sharp.
Should not have
• pictures of items

```html
<!DOCTYPE html>
<html lang="en">
<head>
<meta charset="utf-8">
<title>PeppertonRUN Business Card</title>
<link href="https://fonts.googleapis.com/css2?family=Open+Sans:wght@400;600&display=swap" rel="stylesheet">
<style>
  :root {
    --stage: #25272b;
    --card: #231f20;
    --green: #27a84a;
    --lime: #6cc04a;
    --white: #ffffff;
    --grey: #8a8a8a;
    --gold: #c9b52a;
  }
  * { margin: 0; padding: 0; box-sizing: border-box; }
  html, body { width: 1200px; height: 960px; overflow: hidden; }
  body {
    background: var(--stage);
    font-family: "Open Sans", Arial, sans-serif;
    position: relative;
  }
  .card {
    position: absolute;
    left: 240px;
    width: 720px;
    height: 411px;
    background: var(--card);
    overflow: hidden;
    border-bottom: 4px solid var(--gold);
  }
  .card--front { top: 46px; }
  .card--back { top: 503px; }

  .faint-mark {
    position: absolute;
    background: radial-gradient(ellipse at center, rgba(60,80,40,0.45) 0%, rgba(43,42,34,0.25) 55%, rgba(35,31,32,0) 75%);
  }
  .card--front .faint-mark { right: -60px; top: -40px; width: 460px; height: 420px; }
  .card--back .faint-mark { left: -60px; top: 20px; width: 380px; height: 420px; }

  .brand {
    position: absolute;
    display: flex;
    flex-direction: column;
    align-items: flex-start;
  }
  .brand__row { display: flex; align-items: center; gap: 14px; }
  .brand__dot {
    width: 34px; height: 34px; border-radius: 50%;
    background: var(--lime);
    flex: none;
  }
  .brand__name {
    font-size: 54px;
    font-weight: 400;
    color: var(--white);
    letter-spacing: -0.5px;
    line-height: 1;
  }
  .brand__tagline {
    margin-top: 8px;
    margin-left: 48px;
    font-size: 15px;
    letter-spacing: 2.6px;
    color: var(--grey);
  }
  .card--front .brand { left: 160px; top: 160px; }
  .card--back .brand { left: 40px; top: 178px; }
  .card--back .brand__name { font-size: 40px; }
  .card--back .brand__dot { width: 26px; height: 26px; }
  .card--back .brand__tagline { font-size: 12px; margin-left: 40px; letter-spacing: 2px; }

  .divider {
    position: absolute;
    left: 382px; top: 90px;
    width: 2px; height: 230px;
    background: var(--green);
  }
  .person { position: absolute; left: 420px; top: 88px; }
  .person__name { font-size: 26px; color: var(--green); line-height: 1.2; letter-spacing: -0.5px; }
  .person__role { font-size: 17px; color: var(--white); margin-top: 2px; }

  .contacts { position: absolute; left: 420px; top: 210px; list-style: none; }
  .contacts li {
    display: flex; align-items: center; gap: 10px;
    font-size: 17px; color: var(--white); margin-bottom: 10px;
  }
  .contacts svg { width: 16px; height: 16px; flex: none; }
</style>
</head>
<body>
  <section class="card card--front" aria-label="Card front">
    <div class="faint-mark" role="img" aria-label="Faint enlarged brand decoration"></div>
    <div class="brand">
      <div class="brand__row">
        <span class="brand__dot"></span>
        <span class="brand__name">PeppertonRUN</span>
      </div>
      <span class="brand__tagline">Whole Food, Movement and Care</span>
    </div>
  </section>

  <section class="card card--back" aria-label="Card back">
    <div class="faint-mark" role="img" aria-label="Faint enlarged brand decoration"></div>
    <div class="brand">
      <div class="brand__row">
        <span class="brand__dot"></span>
        <span class="brand__name">PeppertonRUN</span>
      </div>
      <span class="brand__tagline">Whole Food, Movement and Care</span>
    </div>

    <div class="divider"></div>

    <div class="person">
      <p class="person__name">Mara Dulvik Tenbrook</p>
      <p class="person__role">Founder</p>
    </div>

    <ul class="contacts">
      <li>
        <svg viewBox="0 0 16 16"><path d="M4 1 L6.5 4.5 L5 6 Q6.5 9.5 10 11 L11.5 9.5 L15 12 L13 15 Q4 14 1 3 Z" fill="var(--green)"/></svg>
        718-555-0143
      </li>
      <li>
        <svg viewBox="0 0 16 16"><rect x="1" y="3" width="14" height="10" fill="var(--green)"/><path d="M1 3 L8 9 L15 3" stroke="var(--card)" stroke-width="1.5" fill="none"/></svg>
        mara@peppertonrun.com
      </li>
      <li>
        <svg viewBox="0 0 16 16"><circle cx="8" cy="8" r="7" fill="var(--green)"/><ellipse cx="8" cy="8" rx="3" ry="7" stroke="var(--card)" fill="none"/><line x1="1" y1="8" x2="15" y2="8" stroke="var(--card)"/></svg>
        www.peppertonrun.com
      </li>
    </ul>
  </section>
</body>
</html>
```